Residential Construction Design

I'd like a business card that really explains what we do in residential construction. A big name and number, while the other information can be smaller. Since the logo is made up of grays and a teal color, the background may have to stay white? Maybe a subtle gray.(sending 2 different color schemes of the logo for different background color options) I would like a card that just appears "tough" when you look at it.

Industry/Entity Type

Residential

Contact Information for Business Card

Name and logo which will be provided.(Rex Morton Construction, LLC) Rex Morton -Licensed Contractor, Certified Home Inspector. (555) 214-7730 Email: Rmorton_Construction@quellbox.example -Remodeling -Roofs - Siding -Drywall -Decks -Pole Barns -New Construction "Serving Southwest Michigan"

```html
<!DOCTYPE html>
<html lang="en">
<head>
<meta charset="utf-8">
<title>Rex Morton Construction, LLC — Business Card</title>
<link href="https://fonts.googleapis.com/css2?family=Open+Sans:wght@400;700&display=swap" rel="stylesheet">
<style>
  :root {
    --backdrop: #e4e4e2;
    --card: #ffffff;
    --ink: #2b2b2b;
    --gray: #8a8a8a;
    --teal: #22c3ad;
    --rule: #555555;
  }
  * { box-sizing: border-box; margin: 0; padding: 0; }
  html, body {
    width: 1200px; height: 873px; overflow: hidden;
    background: var(--backdrop);
    font-family: "Open Sans", Arial, sans-serif;
  }
  .canvas { position: relative; width: 1200px; height: 873px; }
  .card {
    position: absolute; top: 282px;
    width: 540px; height: 309px;
    background: var(--card);
    box-shadow: 0 2px 6px rgba(0,0,0,.12);
  }
  .card--front { left: 40px; }
  .card--back { left: 620px; display: flex; align-items: center; justify-content: center; }

  .brand { position: absolute; top: 28px; left: 250px; display: flex; align-items: flex-start; gap: 14px; }
  .brand__mark { width: 22px; height: 22px; background: var(--teal); margin-top: 8px; flex: none; }
  .brand__name {
    font-family: "Open Sans", Arial, sans-serif; font-weight: 700;
    color: var(--ink); font-size: 30px; line-height: 1.1;
  }
  .brand__name span { display: block; font-size: 18px; }

  .person { position: absolute; top: 110px; left: 34px; }
  .person__name { font-size: 19px; color: var(--ink); }
  .person__title { font-size: 12.5px; color: var(--gray); line-height: 1.45; }

  .divider { position: absolute; top: 114px; left: 232px; width: 1px; height: 58px; background: var(--rule); transform: rotate(14deg); }

  .contact { position: absolute; top: 112px; left: 258px; color: var(--gray); }
  .contact__email { font-size: 13px; line-height: 1.6; }
  .contact__phone { font-size: 23px; font-weight: 700; color: var(--ink); line-height: 1.4; }

  .services {
    position: absolute; left: 34px; right: 30px; bottom: 46px;
    color: var(--teal); font-weight: 700; font-size: 14px; text-transform: uppercase; line-height: 1.7;
  }
  .services .dot { color: var(--gray); padding: 0 7px; }

  .tagline { position: absolute; left: 34px; bottom: 20px; font-size: 11.5px; color: var(--gray); letter-spacing: .3px; }

  .back-brand { display: flex; align-items: center; gap: 14px; }
  .back-brand .brand__mark { margin-top: 0; }
</style>
</head>
<body>
<main class="canvas">
  <section class="card card--front" aria-label="Business card front">
    <div class="brand">
      <div class="brand__mark"></div>
      <div class="brand__name">Rex Morton<span>Construction, LLC</span></div>
    </div>
    <div class="person">
      <p class="person__name">Rex Morton</p>
      <p class="person__title">Licensed Contractor</p>
      <p class="person__title">Certified Home Inspector</p>
    </div>
    <div class="divider"></div>
    <div class="contact">
      <p class="contact__email">Rmorton_Construction@quellbox.example</p>
      <p class="contact__phone">(555) 214-7730</p>
    </div>
    <div class="services">
      <p>Remodeling<span class="dot">•</span>Roofs<span class="dot">•</span>Siding<span class="dot">•</span>Drywall<span class="dot">•</span>Decks</p>
      <p>Pole Barns<span class="dot">•</span>New Construction</p>
    </div>
    <p class="tagline">Serving Southwest Michigan</p>
  </section>

  <section class="card card--back" aria-label="Business card back">
    <div class="back-brand">
      <div class="brand__mark"></div>
      <div class="brand__name">Rex Morton<span>Construction, LLC</span></div>
    </div>
  </section>
</main>
</body>
</html>
```